Orvel Prime - Letter Head

My company is a residential and commercial cleaning company , which is located in Abu Dhabi, UAE.
I am looking for a creative letterhead reflects the professional and reflects professionalism and send the feeling of relax and comfort.
The color which will be used it has to be selected carefully in prospective of colors psychological effects, so every color to be used should be for a reason.
Also, reflecting my company colors in an attractive way.
Regarding the information which it should contains, it has to show the address, contacts , telephones an, email address and website.
Also, my company logo is attached
Residential

```html
<!DOCTYPE html>
<html lang="en">
<head>
<meta charset="utf-8">
<title>Orvel Prime – Letterhead</title>
<link rel="stylesheet" href="https://fonts.googleapis.com/css2?family=Varela+Round&display=swap">
<style>
  :root {
    --leaf-pale: #e6f3b4;
    --leaf-light: #d9ec8a;
    --leaf-mid: #9fd14a;
    --leaf-deep: #5cb531;
    --leaf-shade: #3f9a28;
    --ink-soft: #5a6b4a;
    --paper: #ffffff;
    --brand-text: #ffffff;
  }
  html, body {
    margin: 0;
    padding: 0;
    overflow: hidden;
    background: var(--paper);
  }
  .letterhead {
    position: relative;
    width: 849px;
    height: 1200px;
    background: var(--paper);
    overflow: hidden;
    font-family: "Varela Round", sans-serif;
  }
  .header-wave {
    position: absolute;
    top: 0;
    left: 0;
    width: 849px;
    height: 170px;
  }
  .brand {
    position: absolute;
    top: 30px;
    left: 40px;
    display: flex;
    align-items: center;
    gap: 14px;
  }
  .brand-name {
    font-size: 36px;
    line-height: 38px;
    color: var(--brand-text);
    margin: 0;
    font-weight: 400;
  }
  .brand-dot {
    width: 64px;
    height: 64px;
    border-radius: 50%;
    border: 3px solid var(--brand-text);
    box-sizing: border-box;
  }
  .contact-block {
    position: absolute;
    left: 40px;
    bottom: 40px;
    width: 480px;
    margin: 0;
    padding-top: 14px;
    border-top: 2px solid var(--leaf-mid);
    font-style: normal;
    font-size: 14px;
    line-height: 24px;
    color: var(--ink-soft);
  }
  .contact-block .contact-line {
    display: flex;
    align-items: center;
    gap: 10px;
    margin: 0;
  }
  .contact-icon {
    width: 14px;
    height: 14px;
    flex: none;
  }
  .sprig-art {
    position: absolute;
    right: 0;
    bottom: 0;
    width: 300px;
    height: 400px;
    border-top-left-radius: 300px 260px;
    background:
      linear-gradient(160deg, var(--leaf-mid) 0%, var(--leaf-deep) 45%, var(--leaf-light) 100%);
    opacity: 0.85;
  }
</style>
</head>
<body>
  <main class="letterhead">
    <svg class="header-wave" viewBox="0 0 849 170" preserveAspectRatio="none" aria-hidden="true">
      <defs>
        <linearGradient id="bandGradient" x1="0" y1="0" x2="1" y2="0">
          <stop offset="0" stop-color="#d9ec8a"/>
          <stop offset="0.45" stop-color="#9fd14a"/>
          <stop offset="1" stop-color="#5cb531"/>
        </linearGradient>
      </defs>
      <path d="M0 0 H849 V78 C720 70 600 100 470 118 C330 138 180 150 0 142 Z" fill="#e6f3b4"/>
      <path d="M0 0 H849 V64 C720 60 600 88 470 104 C330 124 180 138 0 128 Z" fill="url(#bandGradient)"/>
    </svg>

    <div class="brand">
      <p class="brand-name">Orvel<br>Prime</p>
      <span class="brand-dot" aria-hidden="true"></span>
    </div>

    <address class="contact-block">
      <p class="contact-line">
        <svg class="contact-icon" viewBox="0 0 24 24" aria-hidden="true"><path d="M12 2a7 7 0 0 0-7 7c0 5 7 13 7 13s7-8 7-13a7 7 0 0 0-7-7zm0 9.5a2.5 2.5 0 1 1 0-5 2.5 2.5 0 0 1 0 5z" fill="#5cb531"/></svg>
        Office 12, Palm Court, Meridian City
      </p>
      <p class="contact-line">
        <svg class="contact-icon" viewBox="0 0 24 24" aria-hidden="true"><path d="M6.6 10.8a15 15 0 0 0 6.6 6.6l2.2-2.2a1 1 0 0 1 1-.25 11.4 11.4 0 0 0 3.6.57 1 1 0 0 1 1 1V20a1 1 0 0 1-1 1A17 17 0 0 1 3 4a1 1 0 0 1 1-1h3.5a1 1 0 0 1 1 1c0 1.25.2 2.45.57 3.6a1 1 0 0 1-.25 1z" fill="#5cb531"/></svg>
        +00 2 555 0147
      </p>
      <p class="contact-line">
        <svg class="contact-icon" viewBox="0 0 24 24" aria-hidden="true"><path d="M3 5h18v14H3z" fill="none" stroke="#5cb531" stroke-width="2"/><path d="M3 6l9 7 9-7" fill="none" stroke="#5cb531" stroke-width="2"/></svg>
        hello@orvelprime.example
      </p>
      <p class="contact-line">
        <svg class="contact-icon" viewBox="0 0 24 24" aria-hidden="true"><circle cx="12" cy="12" r="9" fill="none" stroke="#5cb531" stroke-width="2"/><path d="M3 12h18M12 3c3 3 3 15 0 18M12 3c-3 3-3 15 0 18" fill="none" stroke="#5cb531" stroke-width="1.6"/></svg>
        www.orvelprime.example
      </p>
    </address>

    <div class="sprig-art" role="img" aria-label="Green plant sprig with dewy leaves on a curved stem"></div>
  </main>
</body>
</html>
```